KB Rubbish Removal Business Card

Hey,
I need a double sided business card designed for a rubbish removal business based in Australia. Logo is already chosen, similar colours preferred for both sides of the business card.

Details to include:

Front:

KB Rubbish Removal
Darren Holloway
Managing Director
Mobile: 0471 902 146
Email: darren@kbrubbishremoval.com.au
Website: kbrubbishremoval.com.au

Rear:

How did we do?
kbrubbishremoval.com.au/review

```html
<!DOCTYPE html>
<html lang="en">
<head>
<meta charset="utf-8">
<title>KB Rubbish Removal – Business Card</title>
<link rel="stylesheet" href="https://fonts.googleapis.com/css2?family=Saira+Condensed:wght@700&family=Roboto:ital,wght@0,400;0,500;1,400&display=swap">
<style>
  :root {
    --backdrop: #222222;
    --card-top: #f2f2f0;
    --card-bottom: #e2e2e0;
    --green: #11893a;
    --green-dark: #0a7a2e;
    --green-light: #7cc242;
    --ink: #2b2b2b;
  }
  * { box-sizing: border-box; margin: 0; padding: 0; }
  html, body { width: 1200px; height: 1138px; overflow: hidden; }
  body { background: var(--backdrop); position: relative; font-family: "Roboto", sans-serif; }

  .card {
    position: absolute;
    width: 620px;
    height: 374px;
    border-radius: 13px;
    overflow: hidden;
    background: linear-gradient(180deg, var(--card-top), var(--card-bottom));
  }
  .card--rear { left: 274px; top: 186px; }
  .card--front { left: 276px; top: 608px; }

  /* logo placeholder: plain name in body font, one plain circle */
  .brand-mark {
    position: absolute;
    display: flex;
    align-items: center;
    gap: 10px;
  }
  .brand-dot {
    flex: none;
    width: 22px;
    height: 22px;
    border-radius: 50%;
    background: var(--green);
  }
  .brand-mark__name {
    font-family: "Roboto", sans-serif;
    font-weight: 500;
    font-size: 20px;
    line-height: 1.2;
    color: var(--green);
    width: 150px;
  }
  .card--rear .brand-mark { left: 40px; top: 160px; }
  .card--front .brand-mark { left: 50px; top: 160px; }

  /* rear side */
  .review-heading {
    position: absolute;
    left: 316px; width: 260px; top: 100px;
    text-align: center;
    font-family: "Saira Condensed", sans-serif;
    font-weight: 700;
    font-size: 56px;
    line-height: 55px;
    color: var(--green);
  }
  .review-link {
    position: absolute;
    left: 316px; width: 260px; top: 234px; height: 31px;
    border-top: 1.5px solid var(--green);
    border-bottom: 1.5px solid var(--green);
    text-align: center;
    font-size: 16.5px;
    line-height: 28px;
    color: var(--green);
  }

  /* front side */
  .company-title {
    position: absolute; left: 291px; top: 76px;
    font-family: "Roboto", sans-serif;
    font-weight: 500;
    font-size: 25px;
    line-height: 1.2;
    color: var(--green);
  }
  .person-name {
    position: absolute; left: 291px; top: 139px;
    font-weight: 500; font-size: 22px; color: var(--green);
  }
  .person-role {
    position: absolute; left: 291px; top: 166px;
    font-size: 15.5px; color: var(--ink);
  }
  .divider {
    position: absolute; left: 291px; top: 193px; width: 223px; height: 1.5px;
    background: linear-gradient(90deg, var(--green), var(--green-light));
  }
  .contact-list { position: absolute; left: 298px; top: 204px; list-style: none; }
  .contact-list li {
    display: flex; align-items: center;
    height: 24px; font-size: 16px; color: var(--ink);
  }
  .contact-list svg { width: 14px; height: 14px; margin-right: 10px; fill: var(--green-dark); }
  .contact-list .accent { color: var(--green); }

  .footer-strip {
    position: absolute; left: 0; bottom: 0; width: 260px; height: 14px;
    background: linear-gradient(90deg, var(--green), var(--green-light));
  }
  .footer-band {
    position: absolute; right: 0; bottom: 0; width: 380px; height: 46px;
    background: linear-gradient(90deg, var(--green-dark), var(--green));
    clip-path: polygon(24px 0, 100% 0, 100% 100%, 0 100%);
  }
  .tagline {
    position: absolute; left: 291px; bottom: 10px;
    font-style: italic; font-size: 16px; color: #ffffff;
  }
</style>
</head>
<body>

  <section class="card card--rear" aria-label="Business card, review side">
    <div class="brand-mark">
      <span class="brand-dot" aria-hidden="true"></span>
      <span class="brand-mark__name">KB Rubbish Removal</span>
    </div>
    <h2 class="review-heading">HOW DID<br>WE DO?</h2>
    <p class="review-link">kbrubbishremoval.com.au/review</p>
  </section>

  <section class="card card--front" aria-label="Business card, contact side">
    <div class="brand-mark">
      <span class="brand-dot" aria-hidden="true"></span>
      <span class="brand-mark__name">KB Rubbish Removal</span>
    </div>
    <h1 class="company-title">KB Rubbish Removal</h1>
    <p class="person-name">Darren Holloway</p>
    <p class="person-role">Managing Director</p>
    <div class="divider"></div>
    <ul class="contact-list">
      <li>
        <svg viewBox="0 0 16 16" aria-hidden="true"><path d="M1 5c0-2 3-3 7-3s7 1 7 3v1h-4V5H5v1H1zM3 7h10l2 7H1z"/></svg>
        0471 902 146
      </li>
      <li>
        <svg viewBox="0 0 16 16" aria-hidden="true"><path d="M1 3h14v10H1zM2.5 4.5 8 9l5.5-4.5v1L8 10 2.5 5.5z" fill-rule="evenodd"/></svg>
        darren@kbrubbishremoval.com.au
      </li>
      <li>
        <svg viewBox="0 0 16 16" aria-hidden="true"><circle cx="8" cy="8" r="7"/><path d="M1 8h14M8 1c-3 3-3 11 0 14M8 1c3 3 3 11 0 14" stroke="#f0f0ee" stroke-width="1" fill="none"/></svg>
        www.<span class="accent">kbrubbishremoval</span>.com.au
      </li>
    </ul>
    <div class="footer-strip"></div>
    <div class="footer-band"></div>
    <p class="tagline">On-time service &amp; friendly staff.</p>
  </section>

</body>
</html>
```